Motivational Poster Design Project

I would like to create a poster with some of my favorite quotes to hang in my office. I did a similar project in 2012 and I've uploaded the top 2 designs so you can get a better idea of what I'm looking for. I will provide feedback on your design within 24 hours of receiving it.

The poster must contain the following quotes:

"You’re only given a little spark of madness. You mustn’t lose it.”
- Dorian Halbrook

“The most contrarian thing of all is not to oppose the crowd but to think for yourself.”
- Marcus Vell

"I constantly see people rise in life who are not the smartest, sometimes not even the most diligent, but they are learning machines. They go to bed every night a little wiser than they were when they got up and boy does that help, particularly when you have a long run ahead of you."
- Walter Brisco

“In theory, there’s no difference between theory and practice. But, in practice, there is.”
- Piet R. K. Ter Wolvenkamp

"At the end of the day, a reactionary life is a normal life. One thing is consistent in every remarkable person: they decide to do something remarkable. Don’t let the world choose who you become."
- Ravindra Kolpe

“It usually takes 3-4 months to try enough that you can do a proper 80/20 analysis, then two months to design systems to scale what *is* working.”
-Gus Ambery

“Authority is 20 percent given, 80 percent taken.”
- Harold Quimsby

“Your actions are consistent with the way the world occurs to you.”
- Anselm Grottke

Project Deadline Extended
Reason: I am going to be travelling with no access to internet until January 5th, 2015. I am extending the project deadline until 12/31/14 and I'll make a final decision during the 1st week of January.

Target Market(s)

Personal Project

Industry/Entity Type

Learning

Requirements
Must have
• The poster will be 24" high x 36" long and printed on canvas, so the image you create needs to have a resolution of at least 2700 x 3900.
Nice to have
• I don't have an exact vision for how the poster should look, so I am totally open to you using your creativity to develop, arrange and present the content as you'd like.
• That said, I would like an image (photo or posterized image) of the person being quoted along with each quote. I do not have specific images that I would like you to use, so you will need to find the images on your own. The images don't need to be perfect... I am more interested in the poster relating the essence of the quotes and the people being quoted than I am in perfect photographic images of the people being quoted.

```html
<!DOCTYPE html>
<html lang="en">
<head>
<meta charset="utf-8">
<title>Quotes Poster</title>
<link href="https://fonts.googleapis.com/css2?family=Roboto+Condensed:wght@400;700&display=swap" rel="stylesheet">
<style>
  :root{
    --paper:#ffffff;
    --bg-center:#eef1f4;
    --bg-edge:#b9c0c8;
    --green:#3c9b37;
    --blue:#1d5ea6;
    --purple:#9b2f96;
    --teal:#1a9fb3;
    --tan:#8a7356;
    --red:#c42a40;
    --emerald:#1f8a58;
    --orange:#c8712c;
    --ink:#ffffff;
    --portrait-a:#9aa1a8;
    --portrait-b:#5d646b;
  }
  html,body{margin:0;padding:0;overflow:hidden;background:var(--paper);}
  .poster{
    position:relative;width:800px;height:1200px;overflow:hidden;
    background:var(--paper);
    font-family:"Roboto Condensed","Arial Narrow",sans-serif;font-weight:700;
  }
  .poster__field{
    position:absolute;left:18px;top:18px;width:764px;height:1164px;
    background:radial-gradient(ellipse at 50% 45%,var(--bg-center) 0%,#dde1e6 55%,var(--bg-edge) 100%);
  }
  .band{
    position:absolute;color:var(--ink);box-sizing:border-box;
    box-shadow:0 3px 8px rgba(0,0,0,.35);
    transform-origin:center;
  }
  .band::before{
    content:"";position:absolute;inset:8px -14px 8px -14px;z-index:-1;
    background:inherit;filter:brightness(.75);
  }
  .quote{margin:0;font-size:20px;line-height:27px;white-space:nowrap;}
  .author{display:block;text-align:right;font-size:16px;line-height:22px;font-weight:400;margin-top:1px;}
  .portrait{
    position:absolute;border:5px solid var(--paper);
    background:linear-gradient(160deg,var(--portrait-a),var(--portrait-b));
    box-shadow:0 3px 10px rgba(0,0,0,.45);z-index:2;
  }
  .band--green{background:var(--green);left:18px;top:40px;width:500px;height:125px;padding:30px 20px 0 200px;transform:rotate(-3deg);}
  .band--blue{background:var(--blue);left:213px;top:160px;width:567px;height:108px;padding:18px 190px 0 14px;transform:rotate(-1.5deg);}
  .band--purple{background:var(--purple);left:18px;top:285px;width:722px;height:195px;padding:20px 14px 0 200px;transform:rotate(-1.8deg);}
  .band--teal{background:var(--teal);left:178px;top:507px;width:602px;height:100px;padding:14px 190px 0 14px;transform:rotate(.6deg);}
  .band--tan{background:var(--tan);left:18px;top:628px;width:662px;height:168px;padding:18px 20px 0 200px;transform:rotate(1.2deg);}
  .band--red{background:var(--red);left:140px;top:805px;width:640px;height:140px;padding:12px 192px 0 16px;transform:rotate(1.8deg);}
  .band--emerald{background:var(--emerald);left:18px;top:955px;width:470px;height:100px;padding:16px 20px 0 185px;transform:rotate(-1.5deg);}
  .band--orange{background:var(--orange);left:298px;top:1060px;width:482px;height:100px;padding:16px 200px 0 16px;transform:rotate(-1.5deg);}
  .p1{left:38px;top:42px;width:146px;height:148px;transform:rotate(-4deg);}
  .p2{left:612px;top:94px;width:138px;height:140px;}
  .p3{left:40px;top:318px;width:142px;height:136px;}
  .p4{left:608px;top:490px;width:138px;height:136px;}
  .p5{left:42px;top:637px;width:143px;height:138px;}
  .p6{left:607px;top:822px;width:140px;height:138px;}
  .p7{left:40px;top:952px;width:143px;height:138px;}
  .p8{left:601px;top:1003px;width:146px;height:142px;}
</style>
</head>
<body>
<div class="poster">
  <div class="poster__field"></div>

  <section class="band band--green"><p class="quote">You’re only given a little spark of<br>madness. You mustn’t lose it.<span class="author">- Dorian Halbrook</span></p></section>
  <div class="portrait p1" role="img" aria-label="Portrait photo of Dorian Halbrook"></div>

  <section class="band band--blue"><p class="quote">The most contrarian thing of all is not to<br>oppose the crowd but to think for yourself.<span class="author">- Marcus Vell</span></p></section>
  <div class="portrait p2" role="img" aria-label="Portrait photo of Marcus Vell"></div>

  <section class="band band--purple"><p class="quote">I constantly see people rise in life who are not the<br>smartest, sometimes not even the most diligent, but they<br>are learning machines. They go to bed every night a little<br>wiser than they were when they got up and boy does that<br>help, particularly when you have a long run ahead of you.<span class="author">- Walter Brisco</span></p></section>
  <div class="portrait p3" role="img" aria-label="Portrait photo of Walter Brisco"></div>

  <section class="band band--teal"><p class="quote">In theory, there's no difference between<br>theory and practice. But, in practice, there is.<span class="author">- Piet R. K. Ter Wolvenkamp</span></p></section>
  <div class="portrait p4" role="img" aria-label="Portrait photo of Piet R. K. Ter Wolvenkamp"></div>

  <section class="band band--tan"><p class="quote">At the end of the day, a reactionary life is a normal<br>life. One thing is consistent in every remarkable<br>person: they decide to do something remarkable.<br>Don’t let the world choose who you become.<span class="author">- Ravindra Kolpe</span></p></section>
  <div class="portrait p5" role="img" aria-label="Portrait photo of Ravindra Kolpe"></div>

  <section class="band band--red"><p class="quote">It usually takes 3-4 months to try enough that you<br>can do a proper 80/20 analysis, then two months<br>to design systems to scale what *is* working.<span class="author">-Gus Ambery</span></p></section>
  <div class="portrait p6" role="img" aria-label="Portrait photo of Gus Ambery"></div>

  <section class="band band--emerald"><p class="quote">Authority is 20 percent given,<br>80 percent taken.<span class="author">- Harold Quimsby</span></p></section>
  <div class="portrait p7" role="img" aria-label="Portrait photo of Harold Quimsby"></div>

  <section class="band band--orange"><p class="quote">Your actions are consistent with<br>the way the world occurs to you.<span class="author">- Anselm Grottke</span></p></section>
  <div class="portrait p8" role="img" aria-label="Portrait photo of Anselm Grottke"></div>
</div>
</body>
</html>
```